Letterhead for louvre roof company in NZ

I require a letter head design for a company called Slatwise Canopy.
I would like a footer to the letter head and possibly a water mark.
See attached logo.

```html
<!DOCTYPE html>
<html lang="en">
<head>
<meta charset="utf-8">
<title>Slatwise Canopy Letterhead</title>
<link rel="stylesheet" href="https://fonts.googleapis.com/css2?family=Open+Sans:wght@400;600&family=Lato:wght@400&display=swap">
<style>
  :root {
    --backdrop: #e4e4e4;
    --paper: #ffffff;
    --ink: #444444;
    --ink-strong: #333333;
    --brand-orange: #f0891f;
    --brand-grey: #b5b5b5;
    --footer-text: #ffffff;
  }
  * { box-sizing: border-box; margin: 0; padding: 0; }
  html, body {
    width: 1040px; height: 1200px; overflow: hidden;
    background: var(--backdrop);
  }
  .letterhead {
    position: absolute; left: 54px; top: 0;
    width: 932px; height: 1200px;
    background: var(--paper);
    font-family: "Open Sans", sans-serif;
    color: var(--ink);
    overflow: hidden;
  }
  .brand {
    position: absolute; left: 0; right: 0; top: 78px;
    display: flex; justify-content: center; align-items: center; gap: 8px;
  }
  .brand-square { width: 12px; height: 12px; background: var(--brand-orange); }
  .brand-name {
    font-family: "Open Sans", sans-serif; font-weight: 600;
    font-size: 17px; color: var(--brand-orange); letter-spacing: 0.3px;
  }
  .letter {
    position: absolute; left: 87px; width: 754px; top: 215px;
    font-size: 15px; line-height: 18px;
  }
  .issue-date { margin-bottom: 18px; }
  .recipient { margin-bottom: 51px; }
  .salutation { margin-bottom: 33px; }
  .body-copy p {
    line-height: 27px; text-align: justify; hyphens: auto;
    margin-bottom: 27px;
  }
  .closing { margin-top: 54px; }
  .signatory {
    margin-top: 64px; font-size: 19px; font-weight: 600; color: var(--ink-strong);
  }
  .signatory-role { margin-top: 6px; font-size: 15px; }
  .footer {
    position: absolute; left: 0; bottom: 0; width: 932px; height: 163px;
  }
  .footer text { font-family: "Lato", sans-serif; fill: var(--footer-text); font-size: 14.5px; }
</style>
</head>
<body>
<main class="letterhead">
  <header class="brand">
    <span class="brand-square"></span>
    <span class="brand-name">Slatwise Canopy</span>
  </header>

  <section class="letter">
    <p class="issue-date">Issuing Date: May 5, 2018</p>
    <p class="recipient">Name Of Employee Mr. XYZABC<br>Address of Employee<br>Address Line 2 etc..</p>
    <p class="salutation">Dear Mr.XYZABC</p>
    <div class="body-copy">
      <p>Lorem Ipsum has been the industry's standard dummy text ever since the 1500s, when an unknown printer took a galley of type and scrambled it to make a type specimen book. It has survived not only five centuries, but also the leap into electronic typesetting, remaining essentially unchanged. It was popularised in the 1960s with the release of Transferline sheets containing Lorem Ipsum passages, and more recently with desktop publishing software like Folio LayoutDesk including versions of Lorem Ipsum.</p>
      <p>Lorem Ipsum is simply dummy text of the printing and typesetting industry. Lorem Ipsum has been the industry's standard dummy text ever since the 1500s, when an unknown printer took a galley of type and scrambled it to make a type specimen book.</p>
      <p>It has survived not only five centuries, but also the leap into electronic typesetting, remaining essentially unchanged. It was popularised in the 1960s with the release of Transferline sheets containing Lorem IpsumIpsum passages.</p>
    </div>
    <p class="closing">Yours Sincerely</p>
    <p class="signatory">Marcus Hale</p>
    <p class="signatory-role">Managing Director</p>
  </section>

  <svg class="footer" viewBox="0 0 789 138" preserveAspectRatio="none" aria-label="Footer band with contact details">
    <path d="M0,5 C110,55 270,88 474,38 C300,74 120,78 0,36 Z" fill="var(--brand-grey)"/>
    <path d="M0,37 C120,76 300,86 474,38 C600,12 700,8 789,18 L789,21 C700,11 600,15 474,41 C300,90 120,80 0,40 Z" fill="#ffffff"/>
    <path d="M0,40 C120,80 300,90 474,41 C600,15 700,11 789,21 L789,138 L0,138 Z" fill="var(--brand-orange)"/>

    <text x="76" y="112">18 Harbour Lane, Auckland 1010, New Zealand</text>

    <text x="691" y="72" text-anchor="end">09-555 0142</text>
    <text x="691" y="90" text-anchor="end">hello@slatwisecanopy.nz</text>
    <text x="691" y="109" text-anchor="end">www.slatwisecanopy.nz</text>

    <g class="icon-phone" fill="#ffffff">
      <path d="M696,63 h12 a2,2 0 0 1 2,2 v2 h-3 v-1.5 h-10 v1.5 h-3 v-2 a2,2 0 0 1 2,-2 Z"/>
      <rect x="697" y="67" width="10" height="6" rx="1"/>
    </g>
    <g class="icon-mail">
      <rect x="696" y="82" width="13" height="9" fill="#ffffff"/>
      <path d="M696,82 L702.5,87.5 L709,82" fill="none" stroke="var(--brand-orange)" stroke-width="1.2"/>
    </g>
    <g class="icon-web">
      <circle cx="702.5" cy="105" r="6.3" fill="#ffffff"/>
      <path d="M699,101 q2,2 0,4 q3,1 2,4 M704,100 q-1,3 2,3 q2,2 1,5" fill="none" stroke="var(--brand-orange)" stroke-width="1.3"/>
    </g>
  </svg>
</main>
</body>
</html>
```